Vel'ora

we need a web design for a new company based in Cameroon called xxx. it is a platform that connects people looking for accommodation (for sale o for rent) with people who offer accommodation, either for a long or short period. we would like to see designs that use the color , the name and logo attached below. we would like a website which monitors a number of people visiting the site; possibilities to connection with all social networks; responsive platform, website mobile friendly. some time ago, we create a logo in motley fern so i have font use, color code and color version. the final design should comunicate trust, and simplicity
An example of website we are looking at is https://www.quintavel.example/

```html
<!DOCTYPE html>
<html lang="en">
<head>
<meta charset="utf-8">
<title>Vel'ora – deal &amp; live</title>
<link href="https://fonts.googleapis.com/css2?family=Archivo:wght@700;800;900&family=Jost:wght@400;500;600&family=Poppins:wght@600;700&display=swap" rel="stylesheet">
<style>
:root{
  --brown:#95561d;
  --brown-dark:#7a4414;
  --green:#143d1e;
  --ink:#1d1d1d;
  --muted:#555;
  --mist:#e2e8ed;
  --night:#17212b;
  --white:#fff;
}
*{box-sizing:border-box;margin:0;padding:0}
html,body{width:1200px;height:4804px;overflow:hidden}
body{font-family:"Jost",sans-serif;color:var(--ink);background:var(--white);position:relative}
.abs{position:absolute}
.photo{display:block}
/* header */
.site-header{position:absolute;top:0;left:0;width:1200px;height:71px;background:#fff;display:flex;align-items:center;border-bottom:2px solid var(--brown)}
.brand{position:absolute;left:112px;top:14px;display:flex;align-items:center;gap:10px;font-family:"Jost",sans-serif;font-weight:600;font-size:30px;color:var(--green)}
.brand-mark{width:34px;height:34px;border:3px solid var(--brown);border-radius:6px}
.main-nav a{position:absolute;top:28px;font-size:14px;color:var(--ink);text-decoration:none}
.lang{position:absolute;left:906px;top:22px;display:flex;align-items:center;gap:6px;font-size:12px}
.lang-dot{width:26px;height:26px;border-radius:50%;background:linear-gradient(#2b3f8c,#c8102e)}
.menu-pill{position:absolute;left:1010px;top:17px;width:76px;height:38px;border:2px solid var(--green);border-radius:20px;display:flex;align-items:center;justify-content:space-between;padding:0 4px 0 10px}
.menu-pill .user{width:30px;height:30px;border-radius:50%;background:var(--green)}
/* hero */
.hero{position:absolute;top:71px;left:0;width:1200px;height:632px;background:linear-gradient(180deg,#b7c9d6 0%,#c9b79a 45%,#8c7a63 75%,#6d5a44 100%)}
.hero-title{position:absolute;top:36px;width:100%;text-align:center;font-family:"Archivo",sans-serif;font-weight:900;font-size:64px;color:#111;letter-spacing:1px}
.search{position:absolute;left:295px;top:123px;width:666px;height:62px;background:#fff;border-radius:31px;box-shadow:0 4px 14px rgba(0,0,0,.15);display:flex;align-items:center}
.search .field{position:absolute;top:14px;font-size:12px;line-height:16px}
.search .field span{display:block;color:#999;font-size:11px}
.search .go{position:absolute;right:8px;top:8px;width:46px;height:46px;border-radius:50%;background:var(--green);display:flex;align-items:center;justify-content:center}
/* shared */
.section-title{font-family:"Archivo",sans-serif;font-weight:800;font-size:38px;color:var(--brown);text-align:center;letter-spacing:.5px}
.section-title::before{content:"";display:inline-block;width:5px;height:32px;background:var(--green);margin-right:20px;vertical-align:-3px}
.btn{position:absolute;height:46px;background:var(--brown);color:#fff;font-size:12px;font-weight:500;letter-spacing:.5px;display:flex;align-items:center;justify-content:space-between;padding:0 10px 0 20px;box-shadow:0 4px 8px rgba(0,0,0,.2)}
.btn .arrow{width:30px;height:30px;border-radius:50%;background:#fff;display:flex;align-items:center;justify-content:center}
/* about */
.about-photo{position:absolute;left:138px;top:793px;width:362px;height:362px;border-radius:50%;border:9px solid var(--brown);background:linear-gradient(160deg,#c9b98f,#6b6b4a 55%,#3f4a55)}
.about-text{position:absolute;left:575px;top:785px;width:492px}
.about-text h2{font-family:"Archivo",sans-serif;font-weight:800;font-size:38px;color:var(--brown);padding-left:24px;border-left:5px solid var(--green)}
.about-text .lead{font-size:20px;font-weight:500;line-height:30px;margin:8px 0 14px;padding-left:24px;border-left:5px solid var(--green)}
.about-text p{font-size:14.5px;line-height:26px;color:var(--muted);text-align:justify}
/* accommodation */
.accommodation{position:absolute;top:1244px;left:0;width:1200px;height:705px;background:var(--mist)}
.accommodation .sub{position:absolute;top:140px;width:100%;text-align:center;font-size:20px;line-height:32px}
.listing-row{position:absolute;top:237px;left:-6px;display:flex;gap:24px}
.listing{width:224px;height:305px;background:#fff;box-shadow:0 3px 8px rgba(0,0,0,.15);flex:none}
.listing .photo{height:164px;background:linear-gradient(170deg,#cfe0ee,#d7c8b3 50%,#7d8a6b)}
.listing h3{font-weight:400;font-size:16px;text-align:center;margin:10px 0 8px}
.listing .specs{display:flex;justify-content:space-around;font-size:15px;color:#444;padding:0 6px;border-bottom:1px solid #ddd;padding-bottom:10px}
.listing .deals{display:flex;font-size:15px}
.listing .deals span{flex:1;text-align:center;padding:12px 0;border-right:1px solid #ddd}
.listing .deals span:last-child{border:none}
/* categories */
.category{position:absolute;top:2108px;width:308px;height:305px;background:#fff;box-shadow:0 3px 10px rgba(0,0,0,.18);text-align:center}
.category .photo{height:164px}
.category h3{font-weight:400;font-size:21px;margin:16px 0 8px}
.category p{font-size:12.5px;color:var(--muted);line-height:21px;padding:0 24px}
.category a{display:inline-block;margin-top:10px;font-size:13px;font-style:italic;color:var(--green)}
/* experiences */
.experiences{position:absolute;top:2594px;left:0;width:1200px;height:797px;background:var(--mist)}
.exp-card{position:absolute;top:173px;width:462px;height:517px;box-shadow:0 5px 14px rgba(0,0,0,.25)}
.exp-card h3{position:absolute;left:16px;top:34px;font-family:"Poppins",sans-serif;font-weight:600;font-size:24px;color:#fff}
.exp-card .btn{left:16px;top:82px;width:175px}
/* places */
.place{position:absolute;top:3551px;width:231px;height:305px;box-shadow:0 4px 10px rgba(0,0,0,.25);display:flex;align-items:flex-end;justify-content:center;padding-bottom:22px;color:#fff;font-size:22px}
/* questions */
.questions{position:absolute;top:4028px;left:0;width:1200px;height:418px;background:linear-gradient(180deg,#2c3a45,#1f2b34 60%,#1b2520);color:#fff;text-align:center}
.questions h2{font-family:"Archivo",sans-serif;font-weight:800;font-size:37px;margin-top:118px}
.questions h2::before{content:"";display:inline-block;width:5px;height:30px;background:#fff;margin-right:20px;vertical-align:-2px}
.questions p{font-size:18px;line-height:30px;width:920px;margin:10px auto 0}
/* footer */
.site-footer{position:absolute;top:4446px;left:0;width:1200px;height:358px;background:var(--night);color:#fff}
.foot-brand{position:absolute;left:152px;top:94px;display:flex;align-items:center;gap:8px;font-size:30px;font-weight:600;color:#2f6a3a}
.foot-brand i{width:26px;height:26px;border:3px solid var(--brown);border-radius:5px}
.socials{position:absolute;left:155px;top:192px;display:flex;gap:8px}
.socials span{width:34px;height:34px;border-radius:50%;border:2px solid var(--brown)}
.foot-col{position:absolute;top:44px}
.foot-col h4{font-weight:400;font-size:16px;margin-bottom:26px}
.foot-col li{list-style:none;font-size:12.5px;line-height:26px}
.contact-item{display:flex;gap:10px;font-size:12.5px;line-height:16px;margin-bottom:20px}
.contact-item small{display:block;color:#aaa;font-size:11px}
.foot-line{position:absolute;left:112px;top:275px;width:1010px;height:1px;background:#3a4752}
.copyright{position:absolute;top:298px;width:100%;text-align:center;font-size:12px}
.to-top{position:absolute;left:1111px;top:250px;width:44px;height:44px;border-radius:50%;background:var(--brown);display:flex;align-items:center;justify-content:center}
</style>
</head>
<body>

<header class="site-header">
  <div class="brand"><span class="brand-mark"></span>Vel'ora</div>
  <nav class="main-nav">
    <a style="left:379px">Recherche</a>
    <a style="left:500px">Cateforie</a>
    <a style="left:610px">Lieu</a>
    <a style="left:683px">Publie une announce</a>
  </nav>
  <div class="lang"><span class="lang-dot"></span>English ⌄</div>
  <div class="menu-pill">
    <svg width="16" height="12"><path d="M0 1h16M0 6h16M0 11h16" stroke="#333" stroke-width="1.5"/></svg>
    <span class="user"></span>
  </div>
</header>

<section class="hero photo" role="img" aria-label="Traveller with suitcase shaking hands with host on a sunny terrace by the sea">
  <h1 class="hero-title">VEL'ORA</h1>
  <div class="search">
    <div class="field" style="left:34px">Where is it<span>Where do you want to go?</span></div>
    <div class="field" style="left:252px">Check in<span>Add dates</span></div>
    <div class="field" style="left:378px">Check-out<span>Add dates</span></div>
    <div class="field" style="left:513px">Guests<span>Add guests</span></div>
    <div class="go"><svg width="18" height="18"><circle cx="7.5" cy="7.5" r="5.5" fill="none" stroke="#fff" stroke-width="2"/><path d="M12 12l5 5" stroke="#fff" stroke-width="2"/></svg></div>
  </div>
</section>

<section class="about">
  <div class="about-photo photo" role="img" aria-label="Backpacker walking through a stone archway courtyard"></div>
  <div class="about-text">
    <h2>ABOUT US</h2>
    <p class="lead">Veritatiset quasiarc hitecto beataevitae dictasunt explicaboemo enimipsamia.</p>
    <p>Perspiciatis unde omnisiste natus error sit voluptatem accusantium doloremque laudantium totamrem aperiam, eaqueipsa quaeabillo inventore veritatisetquasi architecto beatae vitaedictasunt explica boemo enim ipsam voluptatemq uiarspiciatis undeomnisiste natus error sit voluptatem accusantium doloremque laudantium totamrem aperiam, eaqueipsa quae abilloin ventore veritatiset quasi architecto beatae vitaedicta sunt explica boevolup tatemquia.</p>
  </div>
  <div class="btn" style="left:570px;top:1110px;width:183px">LEARN MORE<span class="arrow"><svg width="14" height="10"><path d="M0 5h12M8 1l4 4-4 4" fill="none" stroke="#333" stroke-width="1.5"/></svg></span></div>
</section>

<section class="accommodation">
  <h2 class="section-title" style="position:absolute;top:80px;width:100%">ACCOMMODATION</h2>
  <p class="sub">Veritatiset quasiarc hitecto beataevitae dictasunt<br>explicaboemo enimipsamia.</p>
  <div class="listing-row">
    <article class="listing"><div class="photo" role="img" aria-label="Modern apartment building"></div><h3>CONSECTETUR ADIPISCI</h3><div class="specs"><span>🛏 2bk</span><span>🛁 1br</span><span>▥ 1ba</span></div><div class="deals"><span>BUY</span><span>RENT</span><span>SELL</span></div></article>
    <article class="listing"><div class="photo" role="img" aria-label="Modern apartment building"></div><h3>CONSECTETUR ADIPISCI</h3><div class="specs"><span>🛏 2bk</span><span>🛁 1br</span><span>▥ 1ba</span></div><div class="deals"><span>BUY</span><span>RENT</span><span>SELL</span></div></article>
    <article class="listing"><div class="photo" role="img" aria-label="Modern apartment building"></div><h3>CONSECTETUR ADIPISCI</h3><div class="specs"><span>🛏 2bk</span><span>🛁 1br</span><span>▥ 1ba</span></div><div class="deals"><span>BUY</span><span>RENT</span><span>SELL</span></div></article>
    <article class="listing"><div class="photo" role="img" aria-label="White residential block"></div><h3>CONSECTETUR ADIPISCI</h3><div class="specs"><span>🛏 2bk</span><span>🛁 1br</span><span>▥ 1ba</span></div><div class="deals"><span>BUY</span><span>RENT</span><span>SELL</span></div></article>
    <article class="listing"><div class="photo" role="img" aria-label="Terraced houses with gardens"></div><h3>CONSECTETUR ADIPISCI</h3><div class="specs"><span>🛏 2bk</span><span>🛁 1br</span><span>▥ 1ba</span></div><div class="deals"><span>BUY</span><span>RENT</span><span>SELL</span></div></article>
  </div>
  <div class="btn" style="left:525px;top:574px;width:150px">VIEW ALL<span class="arrow"><svg width="14" height="10"><path d="M0 5h12M8 1l4 4-4 4" fill="none" stroke="#333" stroke-width="1.5"/></svg></span></div>
</section>

<section class="categories">
  <h2 class="section-title" style="position:absolute;top:2026px;width:100%">CATEGORIES</h2>
  <article class="category" style="left:112px"><div class="photo" role="img" aria-label="White apartment building" style="background:linear-gradient(170deg,#bcd6ee,#e6e6e6 55%,#9aa889)"></div><h3>APPARTEMENTS</h3><p>Perspiciatis unde omnisiste natus error sit voluptatem accusantium doloremque</p><a>Learn More →</a></article>
  <article class="category" style="left:445px"><div class="photo" role="img" aria-label="Thatched huts in a forest" style="background:linear-gradient(170deg,#d8e2c8,#8a6a45 55%,#4f5f35)"></div><h3>CHAMBRES</h3><p>Perspiciatis unde omnisiste natus error sit voluptatem accusantium doloremque</p><a>Learn More →</a></article>
  <article class="category" style="left:780px"><div class="photo" role="img" aria-label="Villa with pool and palm trees" style="background:linear-gradient(170deg,#cfe0ef,#5a5046 55%,#4d7c8c)"></div><h3>VILLA</h3><p>Perspiciatis unde omnisiste natus error sit voluptatem accusantium doloremque</p><a>Learn More →</a></article>
  <div class="btn" style="left:525px;top:2462px;width:150px">VIEW ALL<span class="arrow"><svg width="14" height="10"><path d="M0 5h12M8 1l4 4-4 4" fill="none" stroke="#333" stroke-width="1.5"/></svg></span></div>
</section>

<section class="experiences">
  <h2 class="section-title" style="position:absolute;top:82px;width:100%">DISCOVER THE VEL'ORA EXPERIENCES</h2>
  <article class="exp-card photo" style="left:112px;background:linear-gradient(180deg,#3c4a3a,#3e6b3b 35%,#2f8fc0 60%,#1f6aa8)" role="img" aria-label="Resort swimming pool surrounded by tropical trees">
    <h3>Consectetur adipiscing elitsedo</h3>
    <div class="btn">EXPERIENCES<span class="arrow"><svg width="14" height="10"><path d="M0 5h12M8 1l4 4-4 4" fill="none" stroke="#333" stroke-width="1.5"/></svg></span></div>
  </article>
  <article class="exp-card photo" style="left:625px;background:linear-gradient(180deg,#3a3a3a,#6a5a4a 35%,#a88f6e 60%,#4c5a3a)" role="img" aria-label="Traveller with backpack raising arms in a garden">
    <h3>Consectetur adipiscing elitsedo</h3>
    <div class="btn">EXPERIENCES<span class="arrow"><svg width="14" height="10"><path d="M0 5h12M8 1l4 4-4 4" fill="none" stroke="#333" stroke-width="1.5"/></svg></span></div>
  </article>
</section>

<section class="places">
  <h2 class="section-title" style="position:absolute;top:3469px;width:100%">OUR PLACES</h2>
  <div class="place photo" style="left:112px;background:linear-gradient(180deg,#9cc0e0,#6d7f8f 60%,#3a3f3a)" role="img" aria-label="Iron tower against blue sky">Errorsit Volupta</div>
  <div class="place photo" style="left:360px;background:linear-gradient(180deg,#a9c7df,#5d7a4a 55%,#2f4b3a)" role="img" aria-label="Limestone cliffs covered in jungle">Errorsit Volupta</div>
  <div class="place photo" style="left:609px;background:linear-gradient(180deg,#4a5a70,#c79a5a 55%,#5a4030)" role="img" aria-label="Domed stone monument at sunset">Errorsit Volupta</div>
  <div class="place photo" style="left:857px;background:linear-gradient(180deg,#4d7fc0,#b59a70 55%,#5a4a3a)" role="img" aria-label="Gothic cathedral over a city square">Errorsit Volupta</div>
  <div class="btn" style="left:525px;top:3898px;width:150px">VIEW ALL<span class="arrow"><svg width="14" height="10"><path d="M0 5h12M8 1l4 4-4 4" fill="none" stroke="#333" stroke-width="1.5"/></svg></span></div>
</section>

<section class="questions" role="img" aria-label="Mountain cabins at dusk">
  <h2>DO YOU HAVE QUESTIONS ABOUT US?</h2>
  <p>Perspiciatis unde omnisiste natus error sit voluptatem accusantium doloremque laudantium totamrem aperiam, eaqueipsa quaeabillo inventore veritatisetquasi architecto beatae vitaedictasunt explica boemo enim ipsam voluptatemq uiarspiciatis undeomnisiste natus errorsit</p>
  <div class="btn" style="left:525px;top:313px;width:150px;background:#fff;color:var(--ink)">REACH US<span class="arrow" style="background:var(--green)"><svg width="14" height="10"><path d="M0 5h12M8 1l4 4-4 4" fill="none" stroke="#fff" stroke-width="1.5"/></svg></span></div>
</section>

<footer class="site-footer">
  <div class="foot-brand"><i></i>Vel'ora</div>
  <div class="socials"><span></span><span></span><span></span></div>
  <div class="foot-col" style="left:358px"><h4>QUICK LINKS</h4><ul><li>RECHERCHE</li><li>CATEFORIE</li><li>LIEU</li><li>PUBLIE UNE ANNOUNCE</li></ul></div>
  <div class="foot-col" style="left:569px"><h4>LINKS</h4><ul><li>DE NOUS</li><li>FONCTIONNEMENTS</li><li>CONDITIONS</li><li>ASSISTANCES</li><li>PRIVACY</li><li>CONTACTS</li></ul></div>
  <div class="foot-col" style="left:739px"><h4>SUPPORT</h4><ul><li>TEAM</li><li>ABOUT US</li><li>CAREERS</li><li>OUR VALUES</li></ul></div>
  <div class="foot-col" style="left:894px"><h4>CONTACT US</h4>
    <div class="contact-item"><svg width="12" height="16"><path d="M6 15C2 10 1 8 1 6a5 5 0 0110 0c0 2-1 4-5 9z" fill="var(--brown)"/></svg><div><small>Address</small>48, Rue des Palmiers,<br>Douala</div></div>
    <div class="contact-item"><svg width="12" height="14"><path d="M2 1l3 0 1 3-2 1c1 2 2 3 4 4l1-2 3 1v3c-6 0-10-4-10-10z" fill="var(--brown)"/></svg><div><small>Phone</small>+237 (555) 010 2045</div></div>
    <div class="contact-item"><svg width="12" height="14"><rect x="0" y="3" width="12" height="9" fill="var(--brown)"/><path d="M0 3l6 5 6-5" fill="none" stroke="#fff"/></svg><div><small>Email</small>info.velora@mail.com</div></div>
  </div>
  <div class="to-top"><svg width="12" height="8"><path d="M1 7l5-5 5 5" fill="none" stroke="#fff" stroke-width="2"/></svg></div>
  <div class="foot-line"></div>
  <p class="copyright">©2022. ALL RIGHTS RESERVED.</p>
</footer>

</body>
</html>
```